Vocational Mentor needs an impressive business card

1. I need a business card (or maybe three with identic look) to promote me and my three business titles/services:
- Vocational Mentor. I help people find their vocation and live happily from it. I use my 20 years of experience in business, management and psychology to help them identify the most efficient ways to make a living doing what they are passionate about.
- Business Angel. I help founders start a succesful business with minimum risks and costs. I use my 20 years of experience in sales, management and entrepreneurship to help them identify the most efficient ways, in terms of time and cost, to validate their business idea.
- Learning Designer. I design unique learning programs that produce long-term cognitive and behavioural changes to people and organisations. I use my 20 years of experience in learning, teaching and change management to create minimalist experiences and processes that allow them to change efficiently in their pursued direction.

2. I would like a two-sided business card, on the front with my name, contact details and titles, on the back the explanation of the services.
Updates

Hi all,

I updated my brief, included contacts info and give feedback on all designs I got. I am new on this platform so please tell me if you need anything else or if I don't use corectly the platform forms.

Kind regards,
Tudor

Hi all,

I shortened the services description by deleting the phrase "I call..."

Kind regards,
Tudor

Target Market(s)

Freelancers, startups, people and organization willing to invest in change through ultimate learning experiences

Industry/Entity Type

Business

Font styles to use
Serif

Requirements
Must have
• Front side: full name, titles, web site, email, phone like below:
Tudor Vasilache
Vocational Mentor, Business Angel, Learning Designer
info@tudorvasilache.example
www.tudorvasilache.example
+40-745-TUDORV
Nice to have
• Back side: the description of the services I provide as in the task description.
1/3: it would be nice if I can jam all three titles on the front side but then I need a solution to jam all three services on the back side.

```html
<!DOCTYPE html>
<html lang="en">
<head>
<meta charset="utf-8">
<title>Tudor Vasilache – Business Card</title>
<link href="https://fonts.googleapis.com/css2?family=Gelasio:wght@400;700&family=Playfair+Display:wght@500&display=swap" rel="stylesheet">
<style>
  :root {
    --navy: #1f3566;
    --navy-deep: #192c57;
    --gold: #b99a45;
    --gold-light: #e6c46a;
    --paper: #fbfbf9;
    --ink: #2a2a2a;
    --backdrop: #ecebe7;
  }
  * { margin: 0; padding: 0; box-sizing: border-box; }
  html, body {
    width: 1200px; height: 1023px; overflow: hidden;
    background: var(--backdrop);
    font-family: "Gelasio", Georgia, serif;
  }
  .sheet {
    position: relative; width: 1200px; height: 1023px;
    display: flex; flex-direction: column; align-items: center;
    justify-content: center; gap: 60px;
  }
  .card {
    width: 735px; height: 420px; position: relative; overflow: hidden;
    box-shadow: 0 8px 24px rgba(0,0,0,.18);
  }

  /* Back side: services */
  .card-back { display: flex; flex-direction: column; }
  .service {
    color: #fff; padding: 0 44px; display: flex; align-items: center;
    font-size: 16.5px; line-height: 1.28;
  }
  .service strong { font-weight: 700; }
  .service--mentor { background: var(--navy); flex: 0 0 34%; }
  .service--angel { background: var(--gold); flex: 0 0 28%; }
  .service--designer { background: var(--navy); flex: 1; }

  /* Front side: identity */
  .card-front { background: var(--paper); }
  .front-header {
    height: 138px; background: var(--navy);
    display: flex; align-items: center; padding-left: 44px;
    border-bottom: 9px solid var(--gold-light);
  }
  .front-name {
    font-family: "Playfair Display", Georgia, serif; font-weight: 500;
    font-size: 56px; color: #fff; letter-spacing: .5px;
  }
  .front-body {
    position: absolute; left: 44px; right: 44px; bottom: 44px;
    display: flex; justify-content: space-between; align-items: flex-end;
  }
  .holder-name { color: var(--gold-light); font-size: 24px; margin-bottom: 4px; }
  .titles { list-style: none; color: var(--ink); font-size: 18px; line-height: 1.35; }
  .contacts { list-style: none; color: var(--ink); font-size: 16.5px; line-height: 1.55; }
  .contacts li { display: flex; align-items: center; gap: 14px; }
  .contacts svg { width: 16px; height: 16px; fill: var(--gold-light); flex: none; }
</style>
</head>
<body>
<main class="sheet">
  <section class="card card-back" aria-label="Business card back">
    <p class="service service--mentor"><span><strong>Vocational Mentor.</strong> I help people to find their vocation and live happily from it. I use my 20 years of experience in business, management and psychology to help them identify the most efficient ways to make a living doing what they are passionate about.</span></p>
    <p class="service service--angel"><span><strong>Business Angel.</strong> I help founders to start a succesful business with minimum risks and costs. I use my 20 years of experience in sales, management and entrepreneurship to help them identify the most efficient ways, in terms of time and cost, to validate their business idea.</span></p>
    <p class="service service--designer"><span><strong>Learning Designer.</strong> I design unique learning programs that produce long-term cognitive and behavioural changes to people and organisations. I use my 20 years of experience in learning, teaching and change management to create minimalist experiences and processes that allows them to change efficiently in their pursued direction.</span></p>
  </section>

  <section class="card card-front" aria-label="Business card front">
    <header class="front-header"><h1 class="front-name">Tudor Vasilache</h1></header>
    <div class="front-body">
      <div class="identity">
        <p class="holder-name">Tudor Vasilache</p>
        <ul class="titles">
          <li>Vocational Mentor</li>
          <li>Business Angel</li>
          <li>Learning Designer</li>
        </ul>
      </div>
      <ul class="contacts">
        <li><svg viewBox="0 0 16 16" aria-hidden="true"><path d="M2 5c0-2 2-3 6-3s6 1 6 3v1h-3V4.5H5V6H2zM4 7h8l2 6H2zm4 1.5a2 2 0 100 4 2 2 0 000-4z"/></svg>+40-745-TUDORV</li>
        <li><svg viewBox="0 0 16 16" aria-hidden="true"><path d="M1 3h14v1L8 9 1 4zM1 5.5l7 5 7-5V13H1z"/></svg>info@tudorvasilache.example</li>
        <li><svg viewBox="0 0 16 16" aria-hidden="true"><path d="M8 1a7 7 0 100 14A7 7 0 008 1zm0 1.2c.8.8 1.5 2.2 1.7 4.2H6.3C6.5 4.4 7.2 3 8 2.2zM2.3 7.4h3c0 .4 0 .8 0 1.2h-3a5.8 5.8 0 010-1.2zm8.4 0h3a5.8 5.8 0 010 1.2h-3c0-.4 0-.8 0-1.2zM6.3 9.6h3.4c-.2 2-.9 3.4-1.7 4.2-.8-.8-1.5-2.2-1.7-4.2zM6.3 7.4h3.4v1.2H6.3z"/></svg>www.tudorvasilache.example</li>
      </ul>
    </div>
  </section>
</main>
</body>
</html>
```